Italian Restaurant Responsive Wordpress Website Design

Italian Restaurant is looking to create a new responsive website design based on some Wordpress templates that have been selected as favourites. We want to base the influence of the design off a business card that was recently created (attached below).
The design should be based of these templates that will be purchased when selected. All templates are responsive. Please read details of templates to learn more about their functions and features. After we select the designs we can deliver the customizable PSD files.
http://layoutmarket.example/item/tavola-responsive-restaurant-wordpress-theme/full_screen_preview/7316428
http://pelmodesigns.example/themes/?theme=Caldora
http://themes.brightwexel.example/fettora/
http://www.tablekitlayouts.example/
Pages required
Homepage
-Navigation
-Contact info always accessible on all responsive viewports. You may have to include a design for Contact info on mobile viewport to the top of the page.
-Hours of Operation
About Page
Menu
-Styling of content will be very identical to menu's. That will be provided once I receive a copy.
Gallery
Contact Page
-Show a map, Contact Details and a Contact/Feedback Form
We are open to any designs that you want to lay on top of these Template designs. The current site is: www.quartolume.example If you want an indication of content.
Any questions please ask! Enjoy!
Updates
Hello Everyone. I just updated the menu being used in the restaurant as well as the fonts that are being used as we speak. Any questions please email me. Cheers.
Target Market(s)
The Target Market is families and a more distinguished crowd. They offer valued gourmet food but are located in a very high end neighbourhood. Want to deliver home made cuisine that's approachable but yet considered gourmet.
Industry/Entity Type
Business
Look and feel
Each slider illustrates characteristics of the customer's brand and the style your logo design should communicate.

```html
<!DOCTYPE html>
<html lang="en">
<head>
<meta charset="utf-8">
<title>Quarto Lume – Menus</title>
<link rel="stylesheet" href="https://fonts.googleapis.com/css2?family=Lato:wght@400;700&family=Lobster&display=swap">
<style>
:root{
  --red:#a33224;
  --red-bright:#e54a2c;
  --link-red:#d9442a;
  --ink:#333;
  --ink-soft:#555;
  --muted:#8a8a8a;
  --cream:#f3efe6;
  --cream-deep:#ece6d9;
  --white:#fff;
  --footer:#3d3530;
  --footer-field:#4f4741;
  --footer-text:#e6e0d8;
}
*{box-sizing:border-box;margin:0;padding:0}
html,body{width:970px;height:1200px;overflow:hidden}
body{position:relative;font-family:"Lato",sans-serif;background:var(--white);color:var(--ink)}

/* header */
.site-header{position:absolute;left:0;top:0;width:970px;height:60px;background:var(--cream);border-bottom:2px solid #cfc9bf;z-index:3}
.main-nav a{position:absolute;top:35px;font-size:13px;font-weight:700;color:var(--ink);text-decoration:none;letter-spacing:.2px}
.main-nav a.is-active{color:var(--red)}
.brand{position:absolute;left:395px;top:56px;width:180px;height:34px;display:flex;align-items:center;justify-content:center;gap:8px;z-index:4}
.brand-dot{width:12px;height:12px;border-radius:50%;background:var(--red)}
.brand-name{font-size:22px;font-weight:700;color:var(--red)}

.hero{position:absolute;left:0;top:60px;width:970px;height:145px;
  background:radial-gradient(circle at 88% 40%,#d9755e 0,#e9c8b6 18%,transparent 30%),
             radial-gradient(circle at 5% 60%,#9fb27a 0,#d8d6c4 22%,transparent 35%),
             linear-gradient(90deg,#ddd6c8,#efe9df 50%,#e6d7cc)}
.hero-intro{position:absolute;left:113px;top:144px;width:745px;height:61px;background:rgba(245,241,233,.88);padding:12px 18px;z-index:1}
.hero-intro h2{font-size:15px;font-weight:400;color:var(--ink);line-height:18px}
.hero-intro p{font-size:12px;color:var(--ink);line-height:16px}

.submenu{position:absolute;left:157px;top:67px;width:139px;height:149px;background:var(--cream);box-shadow:0 1px 4px rgba(0,0,0,.2);z-index:5;padding-top:10px}
.submenu::before{content:"";position:absolute;top:-6px;left:68px;border:6px solid transparent;border-top:0;border-bottom-color:var(--cream)}
.submenu a{display:block;padding-left:14px;height:28px;line-height:16px;font-size:12.5px;font-weight:700;color:var(--ink);text-decoration:none}
.submenu a.is-current{color:var(--red)}

/* flour band */
.flour-band{position:absolute;left:0;top:205px;width:970px;height:88px;background:var(--red);color:var(--white);text-align:center;font-size:14px;font-weight:700;line-height:17px;padding-top:20px}

/* tabs */
.menu-tabs{position:absolute;left:0;top:293px;width:970px;height:45px;background:var(--cream-deep)}
.menu-tabs a{position:absolute;top:16px;height:29px;font-size:12.5px;font-weight:700;color:var(--ink-soft);text-decoration:none}
.menu-tabs a.is-active{top:16px;left:129px;width:87px;background:var(--white);color:var(--red);text-align:center;padding-top:7px}

/* menu columns */
.menu-col{position:absolute;top:375px;width:230px;text-align:center}
.section-head{color:var(--red);margin-bottom:22px}
.section-head h3{font-size:14px;font-weight:700;line-height:18px;text-transform:uppercase}
.section-head p{font-size:12px;line-height:14px}
.dish{margin-bottom:12px}
.dish.group-start{margin-top:12px}
.dish h4{font-size:12px;font-weight:700;line-height:16px;color:var(--ink)}
.dish .price{font-size:12px;font-weight:700;color:var(--red);line-height:15px}
.dish p{font-size:10.5px;line-height:13px;color:var(--muted)}
.side .dish{margin-bottom:10px}
.salad-box{background:var(--cream-deep);width:228px;height:65px;padding-top:9px;margin:38px 0 19px -0px}
.salad-box.section-head{margin-bottom:19px}

.pager{position:absolute;top:1023px;right:130px;font-size:10px;color:var(--link-red)}
.pager span{color:#999;margin:0 3px}

/* footer */
.site-footer{position:absolute;left:0;top:1050px;width:970px;height:150px;background:var(--footer);color:var(--footer-text)}
.newsletter-title{position:absolute;left:128px;top:24px;font-size:12.5px;letter-spacing:.8px;text-transform:uppercase}
.newsletter-sub{position:absolute;left:128px;top:40px;font-size:11px}
.email-field{position:absolute;left:387px;top:23px;width:265px;height:31px;background:var(--footer-field);border:0;font:italic 11px "Lato",sans-serif;color:#8d847c;padding-left:15px;display:flex;align-items:center}
.signup-btn{position:absolute;left:670px;top:22px;width:148px;height:32px;background:var(--red-bright);color:var(--white);font:15px "Lobster",cursive;display:flex;align-items:center;justify-content:center;border-radius:2px}
.footer-rule{position:absolute;left:100px;top:77px;width:770px;height:1px;background:#5a514b}
.footer-info{position:absolute;left:0;top:97px;width:970px;text-align:center;font-size:11px;line-height:14px}
</style>
</head>
<body>
<header class="site-header">
  <nav class="main-nav">
    <a style="left:128px">HOME</a>
    <a style="left:211px">MENUS</a>
    <a class="is-active" style="left:299px">ABOUT US</a>
    <a style="left:593px">GROUPS</a>
    <a style="left:689px">VIP LIST</a>
    <a style="left:780px">CONTACT</a>
  </nav>
</header>
<div class="brand"><span class="brand-dot"></span><span class="brand-name">Quarto Lume</span></div>

<div class="hero" role="img" aria-label="Photo of fresh mozzarella, basil and ripe tomatoes"></div>
<div class="hero-intro">
  <h2>Our Story</h2>
  <p>Lorem ipsum dolor sit amet, consectetuer adipiscing elit.</p>
</div>

<div class="submenu">
  <a>DINNER</a><a>LUNCH</a><a class="is-current">WINE</a><a>DESSERT</a><a>SPECIALS</a>
</div>

<section class="flour-band">
  ... in Italy flour is classified either as &nbsp;1, 2 or 00 and refers to how finely ground the flour is and how much<br>
  of the bran and germ have been removed. Quarto Lume is the most highly refined and is<br>
  talcum-powder soft.
</section>

<nav class="menu-tabs">
  <a class="is-active">DINNER</a>
  <a style="left:241px">LUNCH</a>
  <a style="left:329px">WINE</a>
  <a style="left:407px">DESSERT</a>
  <a style="left:498px">SPECIALS</a>
</nav>

<section class="menu-col" style="left:128px">
  <div class="section-head"><h3>Pizze/Pizza</h3><p>With tomato base</p></div>
  <div class="dish"><h4>Margherita</h4><div class="price">•12 •16 •20</div><p>Tomato sauce, fresh mozzarella and basil</p></div>
  <div class="dish"><h4>Fior Di Latte</h4><div class="price">•12 •16 •20</div><p>Tomatosauce,<br>fior di lattemozzarella and basil</p></div>
  <div class="dish"><h4>Tonno</h4><div class="price">•12 •16 •20</div><p>Tomato sauce, fresh mozzarella,<br>red onions, capers, blackolives, flakedtuna</p></div>
  <div class="dish"><h4>Margherita</h4><div class="price">•12 •16 •20</div><p>Tomato sauce, fresh mozzarella,<br>red onions, capers, blackolives, flakedtuna</p></div>
  <div class="dish group-start"><h4>Fior Di Latte</h4><div class="price">•12 •16 •20</div><p>Tomato sauce, fresh mozzarella, pepperoni,<br>sausage,sop pressata,<br>prosciutto cotto</p></div>
  <div class="dish"><h4>Fior Di Latte</h4><div class="price">•12 •16 •20</div><p>Tomato sauce, fresh mozzarella and basil</p></div>
  <div class="dish"><h4>Margherita</h4><div class="price">•12 •16 •20</div><p>Tomato sauce, fresh mozzarella and basil</p></div>
  <div class="dish"><h4>Fior Di Latte</h4><div class="price">•12 •16 •20</div><p>Tomato sauce, fresh mozzarella and basil</p></div>
  <div class="dish"><h4>Fior Di Latte</h4><div class="price">•12 •16 •20</div><p>Tomato sauce, fresh mozzarella and basil</p></div>
</section>

<section class="menu-col" style="left:371px">
  <div class="section-head"><h3>Pizze Bianche/ White Pizza</h3><p>With olive oil and fresh herb base</p></div>
  <div class="dish"><h4>Margherita</h4><div class="price">•12 •16 •20</div><p>Tomato sauce, fresh mozzarella and basil</p></div>
  <div class="dish"><h4>Fior Di Latte</h4><div class="price">•12 •16 •20</div><p>Tomatosauce,<br>fior di lattemozzarella and basil</p></div>
  <div class="dish"><h4>Tonno</h4><div class="price">•12 •16 •20</div><p>Tomato sauce, fresh mozzarella,<br>red onions, capers, blackolives, flakedtuna</p></div>
  <div class="dish"><h4>Margherita</h4><div class="price">•12 •16 •20</div><p>Tomato sauce, fresh mozzarella,<br>red onions, capers, blackolives, flakedtuna</p></div>
  <div class="dish group-start"><h4>Fior Di Latte</h4><div class="price">•12 •16 •20</div><p>Tomato sauce, fresh mozzarella, pepperoni,<br>sausage,sop pressata,<br>prosciutto cotto</p></div>
  <div class="dish"><h4>Fior Di Latte</h4><div class="price">•12 •16 •20</div><p>Tomato sauce, fresh mozzarella and basil</p></div>
  <div class="dish"><h4>Margherita</h4><div class="price">•12 •16 •20</div><p>Tomato sauce, fresh mozzarella and basil</p></div>
  <div class="dish"><h4>Fior Di Latte</h4><div class="price">•12 •16 •20</div><p>Tomato sauce, fresh mozzarella and basil</p></div>
  <div class="dish"><h4>Fior Di Latte</h4><div class="price">•12 •16 •20</div><p>Tomato sauce, fresh mozzarella and basil</p></div>
</section>

<section class="menu-col side" style="left:614px;width:228px">
  <div class="section-head" style="margin-bottom:18px"><h3>Zuppa/Soup</h3><p>Subcategory elements to go<br>here and here and here</p></div>
  <div class="dish"><h4>Soup of the Day</h4><div class="price">7</div></div>
  <div class="section-head salad-box"><h3>Insalate / Salads</h3><p>Subcategory elements to go<br>here and here and here</p></div>
  <div class="dish"><h4>Insalata Della Casa</h4><div class="price">10</div><p>Variety of lettuces, cherry tomatoes,<br>red onions, and cucumbers,<br>with honey- Dijon balsamic vinaigrette</p></div>
  <div class="dish"><h4>Insalata Cesare</h4><div class="price">10</div><p>Crisp romaine hearts, herbed croutons,<br>pancetta,and parmigiano with<br>acreamy Caesar dressing</p></div>
  <div class="dish"><h4>Caprese</h4><div class="price">10</div><p>Vine ripe tomatoes and fiordi latte<br>mozzarella cheese topped with fresh basil<br>and extra virgin olive oil</p></div>
  <div class="dish"><h4>Insalata Tonno &amp; Fagioli</h4><div class="price">13</div><p>Flaked tuna, onions, borlotti beans<br>with green sinred winev inaigrette</p></div>
  <div class="dish"><h4>Insalata Di Rucola</h4><div class="price">13</div><p>Arugula,freshly cut pears and shaved<br>parmigianoi nacitrus vinaigrette</p></div>
</section>

<div class="pager">« Previous<span>|</span>Next »</div>

<footer class="site-footer">
  <div class="newsletter-title">Sign up for our newsletter</div>
  <div class="newsletter-sub">and recieve notifications from us</div>
  <div class="email-field">enter your email</div>
  <div class="signup-btn">Signup Today</div>
  <div class="footer-rule"></div>
  <div class="footer-info">Quarto Lume 212 Marrow Lane W. Eastbay, ON (555) 014-2290<br>Copyright © 2013 Tavolo.EX</div>
</footer>
</body>
</html>
```